Skin care line needs a LABEL designed!

Fennow Skin Care... An EARTHY modern boho chic skin care line needs a label designed. It is called Fennow because there are healing crystals in the product. Holistic, yoga feel, Earthy, feminine.

This contest is for 1 cleanser label- 2 different versions:

Gel Cleanser
Milk Cleanser

Label Size: 4.8125 x 4.8125 in

Winner will be selected to do the labels for:
Toner (5 Versions)
Serum (5 Versions)
Moisturizer (3 Versions)
Sample Label and packaging

Please be prepared to quote a price for the additional labels listed.

Inspiring Brands: **Marsk Studio**, Tarbell Organics, Celia Drummet, Quillhaven beauty product brands,

Feel free to separate the logo symbol and use it somewhere else in the design.

Target Market(s)

Women ages 30-60

Industry/Entity Type

Skin Care Product

Requirements
Must have
• Tag Line: Inner Peace- Outer Beauty
• Area for ingredients
• Earthy feel
• Large STEP 1 on the front of packaging
• Disclaimer:
• Note: Metaphysical descriptions and healing properties of crystals are not meant to replace medical advice or treat any condition. For external use only.
Nice to have
• www.fennow-skincare-example.com
Should not have
• Multiple Colors

```html
<!DOCTYPE html>
<html lang="en">
<head>
<meta charset="utf-8">
<title>Fennow Skin Care – Milk Cleanser Label</title>
<link rel="stylesheet" href="https://fonts.googleapis.com/css2?family=Oswald:wght@200;500&family=Libre+Baskerville:wght@400;700&display=swap">
<style>
  :root {
    --page: #ffffff;
    --label: #fbfbfb;
    --teal: #3fd8c7;
    --ink: #7d8382;
    --ink-dark: #5f6564;
    --step: #cfd2d2;
    --leaf-green: #4fae8c;
    --leaf-purple: #7c68a8;
    --leaf-blue: #5a7fa8;
    --leaf-pink: #b57aa6;
  }
  * { margin: 0; padding: 0; box-sizing: border-box; }
  html, body {
    width: 1035px;
    height: 1200px;
    overflow: hidden;
    background: var(--page);
  }
  .label {
    position: absolute;
    left: 304px;
    top: 40px;
    width: 427px;
    height: 1120px;
    background: var(--label);
    box-shadow: 0 0 0 1px #eceeee;
    overflow: hidden;
  }
  .botanical-side {
    position: absolute;
    top: 24px;
    width: 64px;
    height: 930px;
    opacity: 0.55;
  }
  .botanical-side.left {
    left: 0;
    background: linear-gradient(180deg, var(--leaf-purple), var(--leaf-green) 30%, var(--leaf-blue) 50%, var(--leaf-green) 70%, var(--leaf-purple));
    -webkit-mask: linear-gradient(90deg, #000 40%, transparent);
            mask: linear-gradient(90deg, #000 40%, transparent);
  }
  .botanical-side.right {
    right: 0;
    background: linear-gradient(180deg, var(--leaf-green), var(--leaf-purple) 30%, var(--leaf-green) 50%, var(--leaf-blue) 70%, var(--leaf-green));
    -webkit-mask: linear-gradient(270deg, #000 40%, transparent);
            mask: linear-gradient(270deg, #000 40%, transparent);
  }
  .botanical-base {
    position: absolute;
    left: 0;
    bottom: 0;
    width: 100%;
    height: 150px;
    opacity: 0.55;
    background: linear-gradient(90deg, var(--leaf-green), var(--leaf-pink) 35%, var(--leaf-green) 55%, var(--leaf-purple) 80%, var(--leaf-green));
    -webkit-mask: linear-gradient(0deg, #000 45%, transparent);
            mask: linear-gradient(0deg, #000 45%, transparent);
  }
  .centered {
    position: absolute;
    left: 0;
    width: 100%;
    text-align: center;
  }
  .brand-mark {
    position: absolute;
    left: 50%;
    top: 150px;
    width: 92px;
    height: 92px;
    margin-left: -46px;
    border: 3px solid var(--teal);
    border-radius: 50%;
  }
  .brand-name {
    top: 262px;
    font-family: "Libre Baskerville", Georgia, serif;
    font-weight: 400;
    font-size: 33px;
    color: var(--teal);
    letter-spacing: 0.5px;
  }
  .tagline {
    top: 352px;
    font-family: "Libre Baskerville", Georgia, serif;
    font-size: 14px;
    letter-spacing: 2.6px;
    color: var(--ink);
  }
  .tagline .accent { color: var(--teal); }
  .product-name {
    top: 428px;
    font-family: "Oswald", "Arial Narrow", sans-serif;
    font-weight: 500;
    font-size: 60px;
    line-height: 72px;
    color: var(--teal);
    letter-spacing: 1px;
  }
  .step {
    top: 620px;
    font-family: "Oswald", "Arial Narrow", sans-serif;
    font-weight: 200;
    font-size: 78px;
    line-height: 86px;
    color: var(--step);
    letter-spacing: 2px;
  }
  .disclaimer {
    top: 738px;
    left: 78px;
    width: 271px;
    font-family: "Libre Baskerville", Georgia, serif;
    font-size: 12.5px;
    line-height: 16px;
    color: var(--ink);
  }
  .disclaimer strong { color: var(--ink-dark); }
  .website {
    top: 872px;
    font-family: "Oswald", "Arial Narrow", sans-serif;
    font-weight: 500;
    font-size: 15px;
    letter-spacing: 0.5px;
    color: var(--ink);
  }
  .volume {
    top: 930px;
    font-family: "Libre Baskerville", Georgia, serif;
    font-size: 34px;
    color: var(--ink-dark);
  }
</style>
</head>
<body>
  <main class="label">
    <div class="botanical-side left" role="img" aria-label="Watercolour vertical border of leaves, ferns and small flowers"></div>
    <div class="botanical-side right" role="img" aria-label="Watercolour vertical border of leaves, ferns and small flowers"></div>
    <div class="botanical-base" role="img" aria-label="Watercolour band of succulents, leaves and pink blossoms"></div>

    <div class="brand-mark" aria-hidden="true"></div>
    <h1 class="centered brand-name">Fennow Skin Care</h1>
    <p class="centered tagline">Inner <span class="accent">Peace</span> | Outer <span class="accent">Beauty</span></p>

    <h2 class="centered product-name">MILK<br>CLEANSER</h2>
    <p class="centered step">STEP 1</p>

    <p class="centered disclaimer">Metaphysical descriptions and healing properties of crystals are not meant to replace medical advice or treat any condition.<br><strong>For external use only.</strong></p>

    <p class="centered website">WWW.FENNOW-SKINCARE-EXAMPLE.COM</p>
    <p class="centered volume">125 ml</p>
  </main>
</body>
</html>
```